I need a business Card Design for my practice , i am clinical herbalist. I am a herbalist specializing in Lyme disease, autism, autoimmune diseases, difficult to cure diseasesDifficult to cure diseases. In my innovative practice i link traditional medicine, herbs with science, immunologu ,pharmacology.

Industry/Entity Type

Business

Contact Information for Business Card

My company name : OŚRODEK ZIELNIK
My name : Piotr Kaleta
Name of my profession : Fitoterapeuta
In Polish language Fitoterapeuta is Herbalist .

e-mail: piotrkaleta@osrodekzielnik.com
www.osrodek-zielnik.pl
phone : 604 587 231
My company adress : Dąbrowa Sitnicka 41 , 38-415 Lużna
I dont have logo .

Requirements
Nice to have
• My company

```html
<!DOCTYPE html>
<html lang="pl">
<head>
<meta charset="utf-8">
<title>Ośrodek Zielnik – wizytówka</title>
<link rel="stylesheet" href="https://fonts.googleapis.com/css2?family=Montserrat:wght@400;700&display=swap">
<style>
  :root {
    --backdrop: #121212;
    --leaf-green: #6aa51a;
    --leaf-dark: #3f7f12;
    --leaf-light: #8cc63a;
    --paper: #dedede;
    --text-green: #6aa51c;
    --url-grey: #6f6f6f;
    --white: #ffffff;
  }
  * { box-sizing: border-box; margin: 0; padding: 0; }
  html, body { width: 1200px; height: 980px; overflow: hidden; }
  body {
    background: var(--backdrop);
    font-family: "Montserrat", Arial, sans-serif;
    position: relative;
  }
  .card {
    position: absolute;
    left: 274px;
    width: 652px;
    height: 404px;
    overflow: hidden;
    box-shadow: 0 10px 30px rgba(0,0,0,.6);
  }
  .card--front { top: 70px; background: var(--leaf-green); }
  .card--back { top: 505px; background: var(--paper); }
  .card svg.art { position: absolute; inset: 0; }

  .brand-name {
    position: absolute;
    font-weight: 700;
    font-size: 40px;
    line-height: 1;
    letter-spacing: 1px;
    white-space: nowrap;
  }
  .card--front .brand-name { left: 226px; top: 136px; color: var(--white); }
  .card--back .brand-name { left: 118px; top: 182px; color: var(--text-green); }

  .brand-url {
    position: absolute;
    font-size: 11.5px;
    letter-spacing: .3px;
    text-transform: uppercase;
    transform: rotate(-6deg);
    transform-origin: left top;
    white-space: nowrap;
  }
  .card--front .brand-url { left: 230px; top: 198px; color: var(--white); }
  .card--back .brand-url { left: 120px; top: 246px; color: var(--url-grey); }

  .contact {
    position: absolute;
    left: 22px;
    top: 290px;
    color: var(--text-green);
    font-size: 17px;
    line-height: 19.5px;
    font-weight: 400;
  }
</style>
</head>
<body>

<section class="card card--front">
  <svg class="art" width="652" height="404" viewBox="0 0 652 404">
    <defs>
      <linearGradient id="leafBand" x1="0" y1="0" x2="0" y2="1">
        <stop offset="0" stop-color="#5a9a18" stop-opacity="0"/>
        <stop offset=".6" stop-color="#4f8f16" stop-opacity=".85"/>
        <stop offset="1" stop-color="#6fb226"/>
      </linearGradient>
    </defs>
    <path role="img" aria-label="Band of fresh green herb leaves along the diagonal edge"
          d="M0,100 C120,120 250,200 400,245 C500,270 580,290 652,300 L652,352 L0,191 Z"
          fill="url(#leafBand)"/>
    <polygon class="paper-panel" points="0,191 652,352 652,404 0,404" fill="var(--paper)"/>
  </svg>
  <div class="brand-name">OŚRODEK ZIELNIK</div>
  <div class="brand-url">www.osrodek-zielnik.pl</div>
  <div class="contact">
    <p class="contact__name">Piotr Kaleta</p>
    <p class="contact__role">Herbalist</p>
    <p class="contact__phone">Phone: 604 587 231</p>
    <p class="contact__address">Address: Dąbrowa Sitnicka 41 , 38-415 Lużna</p>
    <p class="contact__email">Email: piotrkaleta@osrodekzielnik.com</p>
  </div>
</section>

<section class="card card--back">
  <svg class="art" width="652" height="404" viewBox="0 0 652 404">
    <defs>
      <radialGradient id="leafCornerTop" cx="0" cy="0" r="1">
        <stop offset="0" stop-color="#3f7f12"/>
        <stop offset=".6" stop-color="#6aa51a" stop-opacity=".9"/>
        <stop offset="1" stop-color="#8cc63a" stop-opacity="0"/>
      </radialGradient>
      <radialGradient id="leafCornerBottom" cx="1" cy="1" r="1">
        <stop offset="0" stop-color="#3f7f12"/>
        <stop offset=".6" stop-color="#6aa51a" stop-opacity=".9"/>
        <stop offset="1" stop-color="#8cc63a" stop-opacity="0"/>
      </radialGradient>
    </defs>
    <rect role="img" aria-label="Cluster of green herb leaves in the top left corner"
          x="0" y="0" width="170" height="170" fill="url(#leafCornerTop)"/>
    <rect role="img" aria-label="Cluster of green herb leaves in the bottom right corner"
          x="482" y="234" width="170" height="170" fill="url(#leafCornerBottom)"/>
  </svg>
  <div class="brand-name">OŚRODEK ZIELNIK</div>
  <div class="brand-url">www.osrodek-zielnik.pl</div>
</section>

</body>
</html>
```